Design some Business Cards for hair dressing salon

Attached is an example of an older business card - it needs revamping. It also needs to be able to be printed onto Corvel business cards (54mm x 85mm) (code K47208)

```html
<!DOCTYPE html>
<html lang="en">
<head>
<meta charset="utf-8">
<title>Lulu's Hair Salon – Business Cards</title>
<link href="https://fonts.googleapis.com/css2?family=Delius&display=swap" rel="stylesheet">
<style>
  :root {
    --backdrop: #e9e7e4;
    --card-white: #f8f6f1;
    --salon-red: #c8381f;
    --salon-red-deep: #b02e18;
    --label-red: #a82a17;
    --ink: #1a1a1a;
    --cream-text: #f4ece4;
    --tag-dark: #5a1a0e;
    --art-dark: #2a2a2a;
    --art-light: #8a8a8a;
  }
  * { margin: 0; padding: 0; box-sizing: border-box; }
  html, body {
    width: 1200px; height: 780px; overflow: hidden;
    background: var(--backdrop);
    font-family: "Delius", "Comic Sans MS", cursive;
  }
  .canvas { position: relative; width: 1200px; height: 780px; }

  .card {
    position: absolute;
    width: 520px; height: 330px;
    background: var(--card-white);
    overflow: hidden;
    box-shadow: 0 4px 14px rgba(0,0,0,0.18);
  }
  .card--red   { left: 60px;  top: 60px; }
  .card--white { left: 620px; top: 390px; }

  .band { position: absolute; left: 0; width: 100%; }

  .tagline, .street {
    position: absolute; left: 0; width: 100%;
    text-align: center; font-size: 19px; font-weight: 700;
    line-height: 24px; white-space: nowrap;
  }

  .salon-name {
    position: absolute; font-size: 31px; font-weight: 400;
    line-height: 38px; white-space: nowrap;
  }
  .details {
    position: absolute; text-align: center;
    font-size: 19px; line-height: 22px; white-space: nowrap;
  }
  .details .stylist { font-size: 23px; }
  .details .phone { font-size: 25px; line-height: 30px; margin-top: 4px; }

  .hair-art {
    position: absolute;
    background: radial-gradient(ellipse at 50% 40%, var(--art-dark) 0%, var(--art-dark) 45%, var(--art-light) 80%, transparent 100%);
    border-radius: 45% 45% 40% 40%;
  }

  /* Red variant */
  .card--red .band--main { top: 40px; height: 200px; background: linear-gradient(180deg, var(--salon-red), var(--salon-red-deep)); }
  .card--red .tagline { top: 8px; color: var(--label-red); }
  .card--red .street { top: 256px; color: var(--label-red); }
  .card--red .salon-name { left: 36px; top: 58px; color: var(--card-white); text-shadow: 1px 1px 0 rgba(0,0,0,0.35); }
  .card--red .details { left: 40px; top: 104px; width: 250px; color: var(--ink); }
  .card--red .hair-art { left: 315px; top: 48px; width: 170px; height: 184px; }

  /* White variant */
  .card--white .band--top { top: 0; height: 44px; background: var(--salon-red); }
  .card--white .band--rule { top: 236px; height: 5px; background: var(--salon-red); }
  .card--white .band--bottom { top: 254px; height: 76px; background: var(--salon-red); }
  .card--white .tagline { top: 10px; color: var(--tag-dark); }
  .card--white .street { top: 270px; color: var(--cream-text); }
  .card--white .salon-name { left: 40px; top: 62px; color: var(--ink); }
  .card--white .details { left: 30px; top: 106px; width: 280px; color: var(--ink); }
  .card--white .hair-art { left: 318px; top: 52px; width: 170px; height: 176px; }
</style>
</head>
<body>
<div class="canvas">

  <section class="card card--red">
    <div class="band band--main"></div>
    <p class="tagline">For Guys and Girls</p>
    <h1 class="salon-name">Lulu's Hair Salon</h1>
    <div class="details">
      <p>See <span class="stylist">Marnie</span></p>
      <p>for your next appointment</p>
      <p>or call on</p>
      <p class="phone">5917 2036</p>
    </div>
    <div class="hair-art" role="img" aria-label="Black and white illustration of a woman with flowing hair decorated with flowers and butterflies"></div>
    <p class="street">Tamber Street</p>
  </section>

  <section class="card card--white">
    <div class="band band--top"></div>
    <p class="tagline">For Guys and Girls</p>
    <h1 class="salon-name">Lulu's Hair Salon</h1>
    <div class="details">
      <p>See <span class="stylist">Marnie</span></p>
      <p>for your next appointment or</p>
      <p>call on</p>
      <p class="phone">5917 2036</p>
    </div>
    <div class="hair-art" role="img" aria-label="Black and white illustration of a woman with flowing hair decorated with flowers and butterflies"></div>
    <div class="band band--rule"></div>
    <div class="band band--bottom"></div>
    <p class="street">Tamber Street</p>
  </section>

</div>
</body>
</html>
```